Migration Lawyers

Company: Thornbury & Co Lawyers & Migration Agents

Name: Gavin Rusholt BEc, LLB
Address: Level 19, 71 Pelham Street
Sydney, NSW, Australia 2000

Ph: +61 2 9357 2164
M: 0438261504
E: gavin@permit-nomadra.org.au
W: www.permit-nomadra.org.au

Target Market(s)

Migration Clients

Industry/Entity Type

It Company

Font styles to use
Script

Requirements
Must have
• Logo
Should not have
• Please scale the format to the printing size attached

```html
<!DOCTYPE html>
<html lang="en">
<head>
<meta charset="utf-8">
<title>Thornbury &amp; Co — Business Card</title>
<link rel="stylesheet" href="https://fonts.googleapis.com/css2?family=Oswald:wght@500&family=Roboto:wght@400&family=Playfair+Display:wght@700&display=swap">
<style>
  :root {
    --ink: #1f1f1f;
    --paper: #ececec;
    --white: #ffffff;
    --stage: #d9d6d1;
    --card-w: 760px;
    --card-h: 434px;
    --frame: 44px;
  }
  * { box-sizing: border-box; margin: 0; padding: 0; }
  html, body { width: 1200px; height: 1019px; overflow: hidden; }
  body {
    background: var(--stage);
    display: flex;
    flex-direction: column;
    align-items: center;
    justify-content: center;
    gap: 56px;
  }
  .card {
    position: relative;
    width: var(--card-w);
    height: var(--card-h);
    box-shadow: 0 10px 30px rgba(0,0,0,0.25);
    overflow: hidden;
  }
  /* Front: split checker layout */
  .front { display: flex; }
  .front-half { position: relative; width: 50%; height: 100%; }
  .front-left { background: var(--ink); }
  .front-right { background: var(--paper); }
  .identity-panel {
    position: absolute;
    left: var(--frame); top: var(--frame); bottom: var(--frame); right: 0;
    background: var(--paper);
    padding: 40px 30px 36px 44px;
    display: flex; flex-direction: column; justify-content: space-between;
  }
  .contact-panel {
    position: absolute;
    left: 0; top: var(--frame); bottom: var(--frame); right: var(--frame);
    background: var(--ink);
    padding: 52px 20px 0 34px;
    color: var(--white);
    font-family: 'Roboto', sans-serif;
    font-size: 15px;
  }
  .brand { display: flex; align-items: center; gap: 16px; }
  .brand-mark {
    width: 62px; height: 62px; border-radius: 50%;
    border: 2px solid var(--ink); flex: none;
  }
  .brand-name {
    font-family: 'Playfair Display', serif;
    font-weight: 700; font-size: 26px; color: var(--ink); line-height: 1.1;
  }
  .brand-tagline {
    font-family: 'Playfair Display', serif;
    font-weight: 700; font-size: 11px; color: var(--ink); margin-top: 4px;
  }
  .person-name {
    font-family: 'Oswald', sans-serif; font-weight: 500;
    font-size: 30px; letter-spacing: 1px; color: var(--ink); text-transform: uppercase;
  }
  .person-role {
    font-family: 'Roboto', sans-serif; font-size: 20px; color: var(--ink);
  }
  .contact-list { list-style: none; display: flex; flex-direction: column; gap: 12px; }
  .contact-list li { display: flex; align-items: flex-start; gap: 12px; line-height: 1.35; }
  .contact-list svg { flex: none; width: 16px; height: 16px; margin-top: 1px; }
  /* Back: white frame, dark field */
  .back { background: var(--paper); }
  .back-field {
    position: absolute; inset: var(--frame);
    background: var(--ink);
  }
</style>
</head>
<body>
  <article class="card front">
    <div class="front-half front-left">
      <div class="identity-panel">
        <div class="brand">
          <span class="brand-mark"></span>
          <div>
            <div class="brand-name">Thornbury &amp; Co</div>
            <div class="brand-tagline">Lawyers &amp; Migration Agents</div>
          </div>
        </div>
        <div class="person">
          <div class="person-name">Gavin Rusholt</div>
          <div class="person-role">Managing Director</div>
        </div>
      </div>
    </div>
    <div class="front-half front-right">
      <div class="contact-panel">
        <ul class="contact-list">
          <li>
            <svg viewBox="0 0 16 16"><path fill="#fff" d="M8 0a5.5 5.5 0 0 0-5.5 5.5C2.5 10 8 16 8 16s5.5-6 5.5-10.5A5.5 5.5 0 0 0 8 0zm0 8a2.5 2.5 0 1 1 0-5 2.5 2.5 0 0 1 0 5z"/></svg>
            <span>Level 19, 71 Pelham Street<br>Sydney NSW 2000</span>
          </li>
          <li>
            <svg viewBox="0 0 16 16"><path fill="#fff" d="M3.5 1l2.5 3-1.5 2c1 2 3 4 5 5l2-1.5 3 2.5-1.5 2.5C7 14 2 9 1 2.5z"/></svg>
            <span>+61 2 9357 2164</span>
          </li>
          <li>
            <svg viewBox="0 0 16 16"><rect x="4" y="1" width="8" height="14" rx="1.5" fill="none" stroke="#fff" stroke-width="1.6"/><circle cx="8" cy="12.5" r="0.9" fill="#fff"/></svg>
            <span>0438261504</span>
          </li>
          <li>
            <svg viewBox="0 0 16 16"><rect x="1" y="3" width="14" height="10" rx="1" fill="none" stroke="#fff" stroke-width="1.6"/><path d="M1.5 3.5L8 9l6.5-5.5" fill="none" stroke="#fff" stroke-width="1.6"/></svg>
            <span>gavin@permit-nomadra.org.au</span>
          </li>
          <li>
            <svg viewBox="0 0 16 16"><circle cx="8" cy="8" r="6.5" fill="none" stroke="#fff" stroke-width="1.4"/><ellipse cx="8" cy="8" rx="2.8" ry="6.5" fill="none" stroke="#fff" stroke-width="1.2"/><path d="M1.5 8h13" stroke="#fff" stroke-width="1.2"/></svg>
            <span>www.permit-nomadra.org.au</span>
          </li>
        </ul>
      </div>
    </div>
  </article>

  <article class="card back">
    <div class="back-field"></div>
  </article>
</body>
</html>
```